Business Card Design

I need a business card for company that is a limited company that was originally an off-road vehicle company (atv's side by sides snowmobiles and motorcycles) and I have recently sold the assets of the company that was operating under a different name and have become semi retired. I continue to do maintenance on these types of vehicles and also sell and install parts and accessories. Recently I have also contracted to a snowmobile club to operate their groomer to groom the snowmobile trails. I would like bright and bold colors.
Industry/Entity Type
Club
Contact Information for Business Card
KWT Holdings Ltd.
Marcus Ellery
780-555-0143

```html
<!DOCTYPE html>
<html lang="en">
<head>
<meta charset="utf-8">
<title>KWT Holdings Ltd. – Business Card</title>
<link rel="stylesheet" href="https://fonts.googleapis.com/css2?family=Michroma&family=Open+Sans:wght@300;700&display=swap">
<style>
  :root {
    --backdrop: #e4e4e4;
    --navy-dark: #151c45;
    --navy: #1f2c66;
    --royal: #1f46a3;
    --lime: #c6c922;
    --olive: #6f7a35;
    --paper: #f1f1f1;
    --sky: #0a87c8;
    --ink: #111111;
    --white: #ffffff;
  }
  * { margin: 0; padding: 0; box-sizing: border-box; }
  html, body {
    width: 1200px;
    height: 1200px;
    overflow: hidden;
    background: var(--backdrop);
  }
  .stage {
    position: relative;
    width: 1200px;
    height: 1200px;
  }
  .card {
    position: absolute;
    box-shadow: 0 18px 40px rgba(0,0,0,0.18), 0 3px 8px rgba(0,0,0,0.12);
    overflow: hidden;
  }
  .card-front {
    left: 170px;
    top: 80px;
    width: 340px;
    height: 595px;
    background: linear-gradient(170deg, var(--navy-dark) 0%, var(--navy) 45%, var(--royal) 100%);
  }
  .front-accent {
    position: absolute;
    left: 0;
    top: 0;
    width: 100%;
    height: 230px;
    background: linear-gradient(180deg, var(--lime) 0%, var(--olive) 55%, rgba(31,44,102,0) 100%);
    opacity: 0.85;
  }
  .company-name {
    position: absolute;
    left: 283px;
    bottom: 24px;
    transform-origin: left bottom;
    transform: rotate(-90deg);
    white-space: nowrap;
    font-family: "Michroma", sans-serif;
    font-size: 22px;
    line-height: 1;
    letter-spacing: 2px;
    color: var(--white);
    text-transform: uppercase;
  }
  .card-back {
    left: 360px;
    top: 730px;
    width: 700px;
    height: 400px;
    background: var(--paper);
  }
  .back-band {
    position: absolute;
    left: 0;
    right: 0;
    bottom: 0;
    height: 130px;
    background: var(--sky);
  }
  .contact {
    position: absolute;
    left: 0;
    right: 0;
    top: 178px;
    text-align: center;
    color: var(--ink);
    font-family: "Open Sans", sans-serif;
  }
  .contact-name {
    font-weight: 700;
    font-size: 21px;
    line-height: 1.2;
  }
  .contact-phone {
    font-weight: 300;
    font-size: 36px;
    line-height: 1.15;
    letter-spacing: 0.5px;
  }
</style>
</head>
<body>
<main class="stage">
  <section class="card card-front" aria-label="Business card front">
    <div class="front-accent" role="img" aria-label="Decorative lime accent graphic area"></div>
    <p class="company-name">KWT Holdings Ltd.</p>
  </section>

  <section class="card card-back" aria-label="Business card back">
    <div class="contact">
      <p class="contact-name">Marcus Ellery</p>
      <p class="contact-phone">780-555-0143</p>
    </div>
    <div class="back-band"></div>
  </section>
</main>
</body>
</html>
```